Quiet Lantern Sessions on Mental Health

I would like a website designed that would be used to upload podcasts, videos and written material about mental health. Where people will be being as honest, open and truthful as they can about mental health issues.
I would like it to look calming and soothing. Inspired by Vessaray's paintings and colour schemes.

I am on Profile as Dr Helena Marwick - and twitter as drhelenamarwick

Target Market(s)

Healthcare professionals and users of services who want to think at a deeper level about the nature of mental illness

Number of Pages Required

1 page

```html
<!DOCTYPE html>
<html lang="en">
<head>
<meta charset="utf-8">
<title>Dr Helena Marwick – Quiet Lantern Sessions on Mental Health</title>
<link href="https://fonts.googleapis.com/css2?family=Kanit:wght@400;500&family=Be+Vietnam+Pro:wght@400;500;600&display=swap" rel="stylesheet">
<style>
:root{
  --yellow:#ebde2e;
  --yellow-deep:#d9c81a;
  --cream:#faf7da;
  --ink:#262626;
  --muted:#3d3d3d;
  --field:#eeeeee;
  --black:#000;
  --white:#fff;
}
*{box-sizing:border-box;margin:0;padding:0}
html,body{width:1200px;height:4286px;overflow:hidden}
body{position:relative;background:var(--white);font-family:"Be Vietnam Pro",sans-serif;color:var(--ink)}
.abs{position:absolute}
h1,h2,h3,.brand,.stat-num{font-family:"Kanit",sans-serif;font-weight:500}
.photo{position:absolute;overflow:hidden}
.brand{display:flex;align-items:center;gap:8px;font-size:25px;color:var(--ink)}
.brand-dot{width:26px;height:26px;border-radius:50%;background:var(--yellow)}
.section-title{display:flex;align-items:center;gap:8px;font-size:30px;color:var(--ink)}
.section-title .brand-dot{width:22px;height:22px}

/* header */
.site-header{top:0;left:0;width:1200px;height:78px}
.site-header .brand{position:absolute;left:110px;top:24px}
.main-nav{position:absolute;left:478px;top:31px;display:flex;gap:38px;font-size:15px;font-weight:500}
.search-btn{position:absolute;left:1043px;top:18px;width:44px;height:44px;border-radius:50%;background:var(--yellow);display:flex;align-items:center;justify-content:center}

/* hero */
.hero{top:78px;left:0;width:1200px;height:520px;background:linear-gradient(180deg,#b9c1bd 0%,#5f7a58 30%,#2f4d26 65%,#1f3a16 100%)}
.hero-copy{left:597px;top:195px;color:var(--white)}
.hero-copy .kicker{font-family:"Kanit",sans-serif;font-size:24px}
.hero-copy h1{font-size:42px;line-height:1.2;margin-top:2px}
.hero-copy p{font-size:15px;line-height:30px;width:490px;margin-top:14px;font-weight:500}
.btn-primary{display:inline-flex;align-items:center;gap:12px;background:var(--yellow);color:var(--ink);font-family:"Kanit",sans-serif;font-size:22px;height:55px;padding:0 30px;border-radius:4px;margin-top:22px}
.hero-wave{top:520px;left:0}

/* written material */
.written-title{left:110px;top:690px;font-size:25px}
.written-text{left:110px;top:785px;width:490px;font-size:15px;line-height:34.5px;color:var(--muted)}
.stats{left:110px;top:992px;width:597px;height:98px;background:var(--white);border:2px solid #e4e4e4;border-radius:10px;display:flex;box-shadow:0 4px 14px rgba(0,0,0,.06);z-index:2}
.stat{flex:1;display:flex;flex-direction:column;align-items:center;justify-content:center;border-right:2px solid #e4e4e4}
.stat:last-child{border-right:0}
.stat-num{font-size:31px;color:var(--yellow-deep);line-height:1.1}
.stat-label{font-size:16px;font-weight:600;margin-top:6px}
.written-photo{left:680px;top:682px;width:408px;height:430px;border-radius:8px;background:linear-gradient(160deg,#8c8f8a 0%,#c9c7be 40%,#6f86a4 70%,#d9d0bc 100%)}

/* videos */
.videos-band{left:0;top:1207px;width:1200px;height:258px;background:var(--yellow);border-radius:42px 42px 0 0}
.videos-title{left:0;top:1245px;width:1200px;text-align:center;font-size:30px;font-family:"Kanit",sans-serif;font-weight:500}
.video-frame{left:110px;top:1325px;width:978px;height:384px;border-radius:10px;background:linear-gradient(100deg,#e6e4dc 0%,#b9b49a 35%,#8f8a62 60%,#4d4a3c 85%,#2c2b25 100%)}
.play-btn{left:575px;top:1492px;width:50px;height:50px;border-radius:50%;background:var(--yellow);display:flex;align-items:center;justify-content:center}

/* about */
.about-title{left:0;top:1795px;width:1200px;justify-content:center}
.about-photo{left:148px;top:1910px;width:368px;height:390px;border-radius:8px;background:linear-gradient(180deg,#2a1a14 0%,#5a3426 45%,#c79a86 75%,#e9c7bd 100%)}
.about-copy{left:575px;top:1970px;width:490px}
.about-copy h3{font-size:24px;color:var(--yellow-deep)}
.about-copy p{font-size:15px;line-height:34.5px;color:var(--muted);margin-top:10px}
.socials{display:flex;gap:16px;margin-top:34px}
.social{height:42px;padding:0 14px;border-radius:21px;background:var(--yellow);display:flex;align-items:center;font-size:13px;font-weight:600}

/* podcasts */
.podcasts-title{left:0;top:2380px;width:1200px;justify-content:center}
.podcast-card{top:2488px;width:316px;height:424px;background:var(--white);border-radius:8px;box-shadow:0 3px 12px rgba(0,0,0,.12);overflow:hidden}
.podcast-card .cover{position:relative;height:227px}
.podcast-card .sound{position:absolute;left:135px;top:90px;width:46px;height:46px;border-radius:50%;background:var(--yellow);display:flex;align-items:center;justify-content:center}
.podcast-card h3{font-size:20px;color:var(--yellow-deep);margin:20px 0 0 11px;font-weight:500}
.podcast-card p{font-size:15px;line-height:29px;color:var(--muted);margin:8px 0 0 12px;width:300px}
.btn-small{display:inline-flex;align-items:center;gap:8px;background:var(--yellow);font-size:12px;font-weight:600;height:34px;padding:0 18px;border-radius:4px;margin:16px 0 0 12px}
.slider-dots{left:543px;top:2950px;display:flex;gap:12px}
.slider-dots span{width:30px;height:5px;border-radius:3px;background:#f3ec9e}
.slider-dots span.active{background:var(--yellow-deep)}

/* contact */
.contact-band{left:0;top:3042px;width:1200px;height:258px;background:var(--yellow);border-radius:42px 42px 0 0}
.contact-title{left:0;top:3080px;width:1200px;text-align:center;font-size:30px;font-family:"Kanit",sans-serif;font-weight:500}
.contact-card{left:110px;top:3160px;width:978px;height:385px;background:var(--white);border-radius:8px;box-shadow:0 3px 12px rgba(0,0,0,.08);overflow:hidden;display:flex}
.contact-info{width:405px;background:var(--cream);padding:50px 0 0 44px}
.info-row{display:flex;gap:22px;align-items:flex-start;font-size:16px;line-height:34.5px}
.info-row+.info-row{margin-top:40px}
.info-icon{flex:none;width:52px;height:52px;border-radius:50%;background:var(--yellow);display:flex;align-items:center;justify-content:center;margin-top:-8px}
.contact-form{position:relative;flex:1}
.field{position:absolute;background:var(--field);border-radius:6px;font-size:15px;font-weight:500;padding:18px 0 0 26px;color:var(--ink)}
.submit-btn{position:absolute;top:303px;width:120px;height:43px;background:var(--yellow);border-radius:4px;display:flex;align-items:center;justify-content:center;gap:8px;font-size:16px;font-weight:600}

/* testimonials */
.testi-title{left:110px;top:3645px}
.testi-intro{left:112px;top:3727px;width:300px;font-size:15px;line-height:29px;color:var(--muted)}
.stars{left:110px;top:3860px;display:flex;gap:11px}
.testi-photo{left:500px;top:3680px;width:150px;height:172px;border-radius:4px;background:linear-gradient(180deg,#d9d7d4 0%,#b9a08c 45%,#e8e6e2 100%)}
.quote-mark{left:675px;top:3688px;font-family:"Kanit",sans-serif;font-size:34px;line-height:1}
.testi-quote{left:675px;top:3715px;width:420px;font-size:15px;line-height:29px;color:var(--muted)}
.testi-name{left:675px;top:3812px;font-family:"Kanit",sans-serif;font-size:21px;color:var(--yellow-deep)}
.arrow-btn{top:3843px;width:30px;height:30px;border-radius:50%;background:var(--yellow);display:flex;align-items:center;justify-content:center}

/* footer */
.footer-wave{left:0;top:3915px}
.site-footer{left:0;top:3990px;width:1200px;height:296px;background:var(--black);color:var(--white)}
.site-footer .brand{position:absolute;left:0;width:1200px;justify-content:center;top:45px;color:var(--white);font-size:32px}
.site-footer .brand-dot{width:30px;height:30px}
.footer-nav{position:absolute;top:112px;left:0;width:1200px;display:flex;justify-content:center;gap:38px;font-size:16px;font-weight:600}
.footer-social{position:absolute;top:162px;left:0;width:1200px;display:flex;justify-content:center;gap:16px}
.footer-social .social{color:var(--ink)}
.copyright{position:absolute;top:235px;left:0;width:1200px;text-align:center;font-size:14px;font-weight:500;word-spacing:2px}
</style>
</head>
<body>

<header class="abs site-header">
  <div class="brand"><span class="brand-dot"></span>Dr Helena Marwick</div>
  <nav class="main-nav"><span>Home</span><span>About Me</span><span>Testimonials</span><span>Contact Us</span></nav>
  <div class="search-btn" aria-label="Search">
    <svg width="18" height="18" viewBox="0 0 18 18" fill="none" stroke="#222" stroke-width="2"><circle cx="7.5" cy="7.5" r="5.5"/><path d="M12 12l4.5 4.5"/></svg>
  </div>
</header>

<section class="abs hero" role="img" aria-label="Person meditating on a hilltop above misty green forested mountains"></section>
<div class="abs hero-copy">
  <div class="kicker">Welcome To</div>
  <h1>Dr Helena Marwick.</h1>
  <p>Sed ut perspiciatis unde omnis iste natus error sit voluptatem accusantium doloremque laudantium</p>
  <span class="btn-primary">Get Started
    <svg width="24" height="24" viewBox="0 0 24 24" fill="none" stroke="#222" stroke-width="1.8"><circle cx="12" cy="12" r="10.5"/><path d="M8.5 15.5l7-7M10 8.5h5.5V14"/></svg>
  </span>
</div>
<svg class="abs hero-wave" width="1200" height="80" viewBox="0 0 1200 80">
  <path d="M0 78 C220 30 420 60 620 46 C820 32 1000 12 1200 72 V80 H0Z" fill="var(--yellow)"/>
  <path d="M0 80 C220 46 420 74 620 62 C820 50 1000 30 1200 80Z" fill="#fff"/>
</svg>

<h2 class="abs section-title written-title"><span class="brand-dot"></span>Written Material About Mental Health</h2>
<p class="abs written-text">Lorem ipsum dolor sit amet, consectetur adipiscing elit, sed do eiusmod tempor incididunt ut labore et dolore magna aliqua. Ut enim ad minim veniam, quis nostrud exercitation ullamco laboris nisi ut aliquip ex ea commodo consequat. Duis aute irure dolor in reprehenderit in voluptate velit esse cillum dolore eu fugiat nulla</p>
<div class="photo written-photo" role="img" aria-label="Smiling man in a blazer meditating cross-legged on a bench"></div>
<div class="abs stats">
  <div class="stat"><span class="stat-num">14K+</span><span class="stat-label">Happy Clients</span></div>
  <div class="stat"><span class="stat-num">72%</span><span class="stat-label">Problems Sloved</span></div>
  <div class="stat"><span class="stat-num">130+</span><span class="stat-label">Certified Expert</span></div>
</div>

<div class="abs videos-band"></div>
<h2 class="abs videos-title">Videos</h2>
<div class="photo video-frame" role="img" aria-label="Therapy session video: a woman on a sofa talking with a client"></div>
<div class="abs play-btn" aria-label="Play video">
  <svg width="18" height="18" viewBox="0 0 18 18"><circle cx="9" cy="9" r="9" fill="#111"/><path d="M7 5l6 4-6 4z" fill="var(--yellow)"/></svg>
</div>

<h2 class="abs section-title about-title"><span class="brand-dot"></span>About Me</h2>
<div class="photo about-photo" role="img" aria-label="Portrait of Dr Helena Marwick"></div>
<div class="abs about-copy">
  <h3>Dr Helena Marwick</h3>
  <p>Consultant Psychiatrist and Psychotherapist: Lead of a Working Group on Crisis Care and Clinician Wellbeing, Co-Lead of a Patient Safety Forum, Tutor in Reflective Practice, Psychoanalyst, Group Analyst</p>
  <div class="socials"><span class="social">Profile</span><span class="social">Updates</span></div>
</div>

<h2 class="abs section-title podcasts-title"><span class="brand-dot"></span>Podcasts</h2>
<article class="abs podcast-card" style="left:116px">
  <div class="cover" role="img" aria-label="Counsellor taking notes during a session" style="background:linear-gradient(135deg,#d7d6d2,#8e99a6 60%,#c9c3b8)">
    <span class="sound"><svg width="20" height="18" viewBox="0 0 20 18"><path d="M2 6h4l5-4v14l-5-4H2z" fill="#111"/><path d="M14 5c1.5 1.2 1.5 6.8 0 8M16.5 3c3 2.5 3 9.5 0 12" stroke="#111" stroke-width="1.6" fill="none"/></svg></span>
  </div>
  <h3>Duis aute irure exercitation</h3>
  <p>Sed ut perspiciatis unde omnis iste natus error sit voluptatem accusantium</p>
  <span class="btn-small">Learn More <svg width="14" height="14" viewBox="0 0 24 24" fill="none" stroke="#222" stroke-width="2"><circle cx="12" cy="12" r="10"/><path d="M8.5 15.5l7-7M10 8.5h5.5V14"/></svg></span>
</article>
<article class="abs podcast-card" style="left:443px">
  <div class="cover" role="img" aria-label="Stressed person at a laptop surrounded by paperwork" style="background:linear-gradient(135deg,#f1f1f1,#b8b8b8 55%,#e4e4e4)">
    <span class="sound"><svg width="20" height="18" viewBox="0 0 20 18"><path d="M2 6h4l5-4v14l-5-4H2z" fill="#111"/><path d="M14 5c1.5 1.2 1.5 6.8 0 8M16.5 3c3 2.5 3 9.5 0 12" stroke="#111" stroke-width="1.6" fill="none"/></svg></span>
  </div>
  <h3>Lorem ipsum dolor sit</h3>
  <p>Sed ut perspiciatis unde omnis iste natus error sit voluptatem accusantium</p>
  <span class="btn-small">Learn More <svg width="14" height="14" viewBox="0 0 24 24" fill="none" stroke="#222" stroke-width="2"><circle cx="12" cy="12" r="10"/><path d="M8.5 15.5l7-7M10 8.5h5.5V14"/></svg></span>
</article>
<article class="abs podcast-card" style="left:769px">
  <div class="cover" role="img" aria-label="Therapist with a clipboard seated in a bright office" style="background:linear-gradient(135deg,#e7e9ea,#7f97b5 55%,#d6d0c6)">
    <span class="sound"><svg width="20" height="18" viewBox="0 0 20 18"><path d="M2 6h4l5-4v14l-5-4H2z" fill="#111"/><path d="M14 5c1.5 1.2 1.5 6.8 0 8M16.5 3c3 2.5 3 9.5 0 12" stroke="#111" stroke-width="1.6" fill="none"/></svg></span>
  </div>
  <h3>Nemo enim ipsam voluptatem</h3>
  <p>Sed ut perspiciatis unde omnis iste natus error sit voluptatem accusantium</p>
  <span class="btn-small">Learn More <svg width="14" height="14" viewBox="0 0 24 24" fill="none" stroke="#222" stroke-width="2"><circle cx="12" cy="12" r="10"/><path d="M8.5 15.5l7-7M10 8.5h5.5V14"/></svg></span>
</article>
<div class="abs slider-dots"><span></span><span class="active"></span><span></span></div>

<div class="abs contact-band"></div>
<h2 class="abs contact-title">Contact Us</h2>
<section class="abs contact-card">
  <div class="contact-info">
    <div class="info-row"><span class="info-icon"><svg width="20" height="20" viewBox="0 0 24 24" fill="none" stroke="#111" stroke-width="2"><path d="M5 3h4l2 5-2.5 1.5a11 11 0 006 6L16 13l5 2v4a2 2 0 01-2 2A17 17 0 013 5a2 2 0 012-2z"/></svg></span><span>+1 555 014 2290</span></div>
    <div class="info-row"><span class="info-icon"><svg width="20" height="16" viewBox="0 0 20 16"><rect x="1" y="1" width="18" height="14" rx="2" fill="#111"/><path d="M2 2l8 7 8-7" stroke="var(--yellow)" stroke-width="1.6" fill="none"/></svg></span><span>DrHelenaMarwick@lanternmail.com</span></div>
    <div class="info-row"><span class="info-icon"><svg width="18" height="22" viewBox="0 0 18 22"><path d="M9 1a8 8 0 00-8 8c0 6 8 12 8 12s8-6 8-12a8 8 0 00-8-8z" fill="#111"/><circle cx="9" cy="9" r="3" fill="var(--yellow)"/></svg></span><span>Dr Helena Marwick,<br>Hovemoor, England,<br>United Kingdom</span></div>
  </div>
  <form class="contact-form">
    <div class="field" style="left:17px;top:48px;width:264px;height:53px">First Name</div>
    <div class="field" style="left:297px;top:48px;width:264px;height:53px">Last Name</div>
    <div class="field" style="left:17px;top:121px;width:264px;height:53px">Email Address</div>
    <div class="field" style="left:297px;top:121px;width:264px;height:53px">Phone Number</div>
    <div class="field" style="left:17px;top:194px;width:544px;height:80px">Type Your Message</div>
    <span class="submit-btn" style="left:224px">Submit <svg width="16" height="16" viewBox="0 0 24 24" fill="none" stroke="#222" stroke-width="2"><circle cx="12" cy="12" r="10"/><path d="M8.5 15.5l7-7M10 8.5h5.5V14"/></svg></span>
  </form>
</section>

<h2 class="abs section-title testi-title"><span class="brand-dot"></span>Testimonials</h2>
<p class="abs testi-intro">Neque porro quisquam est, qui dolorem ipsum quia dolor sit amet, consectetur, adipisci velit, sed quia non numquam eius modi tempora incidunt ut labore et</p>
<div class="abs stars">
  <svg width="20" height="19" viewBox="0 0 20 19"><path d="M10 0l3 6.5 7 .8-5.2 4.8 1.4 6.9L10 15.5 3.8 19l1.4-6.9L0 7.3l7-.8z" fill="var(--yellow-deep)"/></svg>
  <svg width="20" height="19" viewBox="0 0 20 19"><path d="M10 0l3 6.5 7 .8-5.2 4.8 1.4 6.9L10 15.5 3.8 19l1.4-6.9L0 7.3l7-.8z" fill="var(--yellow-deep)"/></svg>
  <svg width="20" height="19" viewBox="0 0 20 19"><path d="M10 0l3 6.5 7 .8-5.2 4.8 1.4 6.9L10 15.5 3.8 19l1.4-6.9L0 7.3l7-.8z" fill="var(--yellow-deep)"/></svg>
  <svg width="20" height="19" viewBox="0 0 20 19"><path d="M10 0l3 6.5 7 .8-5.2 4.8 1.4 6.9L10 15.5 3.8 19l1.4-6.9L0 7.3l7-.8z" fill="var(--yellow-deep)"/></svg>
  <svg width="20" height="19" viewBox="0 0 20 19"><path d="M10 0l3 6.5 7 .8-5.2 4.8 1.4 6.9L10 15.5 3.8 19l1.4-6.9L0 7.3l7-.8z" fill="var(--yellow-deep)"/></svg>
</div>
<div class="photo testi-photo" role="img" aria-label="Portrait of a smiling client in a white t-shirt"></div>
<div class="abs quote-mark">&ldquo;</div>
<p class="abs testi-quote">Lorem ipsum dolor sit amet, consectetur adipiscing elit, sed do eiusmod tempor incididunt ut labore et dolore magna aliqua. Ut enim ad minim veniam, quis nostrud</p>
<div class="abs testi-name">Lorem Lipsum</div>
<span class="abs arrow-btn" style="left:981px"><svg width="10" height="12" viewBox="0 0 10 12"><path d="M7 1L2 6l5 5" stroke="#111" stroke-width="2" fill="none"/></svg></span>
<span class="abs arrow-btn" style="left:1025px"><svg width="10" height="12" viewBox="0 0 10 12"><path d="M3 1l5 5-5 5" stroke="#111" stroke-width="2" fill="none"/></svg></span>

<svg class="abs footer-wave" width="1200" height="80" viewBox="0 0 1200 80">
  <path d="M0 20 C200 70 420 80 620 66 C820 52 1000 40 1200 6 V80 H0Z" fill="var(--yellow)"/>
  <path d="M0 34 C200 80 420 92 620 80 C820 66 1000 54 1200 22 V80 H0Z" fill="#000"/>
</svg>
<footer class="abs site-footer">
  <div class="brand"><span class="brand-dot"></span>Dr Helena Marwick</div>
  <nav class="footer-nav"><span>Home</span><span>About Me</span><span>Testimonials</span><span>Contact Us</span></nav>
  <div class="footer-social"><span class="social">Profile</span><span class="social">Updates</span></div>
  <p class="copyright">Copyright © 2023 &nbsp; I &nbsp; Dr Helena Marwick &nbsp; I &nbsp; All rights reserved.</p>
</footer>

</body>
</html>
```